Baseline Court Partners needs a business card

I need a business card design for a new company
For the last 10 years I have ran a tennis management company called Silver Ridge Racquet (www.silverridgeracquet.example)
The new company - Baseline Court Partners (BCP) will replace SRRA starting this winter
The goal of BCP will be to expand our operations into new clubs as well and a revenue stream from existing clubs with courtdeskhub.example
We plan to go regional in 2014 and then look outward from there

Target Market(s)

small to medium sized tennis facilities both public and private
Our market are the clubs - not the players
This includes private clubs, municipalities, recreation assc, etc

Industry/Entity Type

Business

Requirements
Must have
• Glen Harwick
• President
• 555-204-1839 Office
• 555-317-9052 Cell
• gharwick@baselinecourtpartners.example
• www.baselinecourtpartnres.example
Nice to have
• One of the unique benefits to a company joining BCP will be integration into our web based club software service - Courtdeskhub.example
• We have developed this turnkey service for small to medium sized clubs and re the exclusive providers of it
Should not have
• address or state

```html
<!DOCTYPE html>
<html lang="en">
<head>
<meta charset="utf-8">
<title>Baseline Court Partners — Business Card</title>
<link rel="stylesheet" href="https://fonts.googleapis.com/css2?family=Montserrat:wght@400;600;700&display=swap">
<style>
  :root {
    --backdrop: #ecebe8;
    --card: #ffffff;
    --ink: #4a4a4a;
    --ink-soft: #6d6d6d;
    --rule: #dcdcdc;
    --accent: #f5c518;
    --accent-deep: #e9b10c;
  }
  * { box-sizing: border-box; margin: 0; padding: 0; }
  html, body {
    width: 1200px; height: 675px; overflow: hidden;
    background: var(--backdrop);
    font-family: "Montserrat", sans-serif;
    color: var(--ink);
  }
  .sheet {
    width: 1200px; height: 675px;
    display: flex; align-items: center; justify-content: center; gap: 60px;
  }
  .card {
    position: relative;
    width: 530px; height: 303px;
    background: var(--card);
    box-shadow: 0 6px 22px rgba(0,0,0,0.12);
  }
  .brand {
    display: flex; align-items: center; gap: 10px;
    font-weight: 400; color: var(--ink-soft); letter-spacing: 0.3px;
    white-space: nowrap;
  }
  .brand-dot { flex: none; border-radius: 50%; background: var(--accent); }

  /* front */
  .card--front .brand {
    position: absolute; left: 0; right: 0; top: 104px;
    justify-content: center; font-size: 30px;
  }
  .card--front .brand-dot { width: 18px; height: 18px; }
  .card--front .site {
    position: absolute; left: 0; right: 0; bottom: 70px;
    text-align: center; font-size: 15px; font-weight: 600;
    color: var(--ink-soft); letter-spacing: 0.4px;
  }

  /* back */
  .card--back .brand {
    position: absolute; right: 34px; top: 36px; font-size: 21px;
  }
  .card--back .brand-dot { width: 13px; height: 13px; }
  .divider {
    position: absolute; right: 34px; top: 84px;
    width: 280px; height: 1px; background: var(--rule);
  }
  .contact {
    position: absolute; right: 34px; top: 96px;
    list-style: none;
    font-size: 12px; line-height: 20px; color: var(--ink-soft);
  }
  .contact li { display: flex; align-items: center; justify-content: flex-end; gap: 7px; white-space: nowrap; }
  .contact svg { flex: none; width: 11px; height: 11px; fill: var(--accent); }

  .person {
    position: absolute; left: 30px; top: 178px; width: 230px;
  }
  .person-name { font-size: 17px; font-weight: 700; color: var(--accent-deep); }
  .person-role { font-size: 13px; color: var(--ink); margin-top: 1px; }
  .person-rule { height: 2px; background: var(--accent); margin: 6px 0; }
  .person-lines { list-style: none; font-size: 11.5px; line-height: 18px; color: var(--ink-soft); }
  .person-lines li { display: flex; align-items: center; gap: 7px; white-space: nowrap; }
  .person-lines svg { flex: none; width: 10px; height: 10px; fill: var(--accent); }
</style>
</head>
<body>
<main class="sheet">
  <section class="card card--front" aria-label="Card front">
    <div class="brand"><span class="brand-dot"></span><span class="brand-name">Baseline Court Partners</span></div>
    <p class="site">www.baselinecourtpartnres.example</p>
  </section>

  <section class="card card--back" aria-label="Card back">
    <div class="brand"><span class="brand-dot"></span><span class="brand-name">Baseline Court Partners</span></div>
    <div class="divider"></div>
    <ul class="contact">
      <li>gharwick@baselinecourtpartners.example
        <svg viewBox="0 0 10 10" aria-hidden="true"><path d="M0 2h10v6H0z"/></svg></li>
      <li>www.baselinecourtpartnres.example
        <svg viewBox="0 0 10 10" aria-hidden="true"><circle cx="5" cy="5" r="4"/></svg></li>
      <li>Courtdeskhub.example
        <svg viewBox="0 0 10 10" aria-hidden="true"><rect x="1" y="1" width="8" height="8"/></svg></li>
    </ul>
    <div class="person">
      <p class="person-name">Glen Harwick</p>
      <p class="person-role">President</p>
      <div class="person-rule"></div>
      <ul class="person-lines">
        <li><svg viewBox="0 0 10 10" aria-hidden="true"><path d="M1 3h8v6H1zM3 1h4v2H3z"/></svg>555-204-1839 Office</li>
        <li><svg viewBox="0 0 10 10" aria-hidden="true"><rect x="2.5" y="0" width="5" height="10" rx="1"/></svg>555-317-9052 Cell</li>
      </ul>
      <div class="person-rule"></div>
    </div>
  </section>
</main>
</body>
</html>
```